Mobile Auto Repair Facebook Ad

We need a facebook ad designed for our mobile mechanic business. Our website is www.kellbrightmotorworks.com and main line is (940) 572-9163

We do all types of auto maintenance/repair on customer vehicles at their home/office or wherever! We'd like to focus on the convenience of a mobile mechanic in the ad versus taking it to a shop!

Target Market(s)

18 and up, Men & Women, 5 mile radius of business location in Denton, TX

Industry/Entity Type

Auto Repair

Font styles to use
Serif

Colors

Designer to choose colors to be used in the design.

Requirements
Must have
• I'd like to have a service van in the ad at a customers house.
Nice to have
• Maybe a car being worked on in the background or a technician greeting a customer.

```html
<!DOCTYPE html>
<html lang="en">
<head>
<meta charset="utf-8">
<title>Kellbright Motorworks – Mobile Auto Repair Ad</title>
<link href="https://fonts.googleapis.com/css2?family=Montserrat:wght@600&family=Roboto+Condensed:wght@500;700&family=Arimo:wght@700&display=swap" rel="stylesheet">
<style>
  :root {
    --ink-dark: #1b1b1b;
    --ink-mid: #3a3a3a;
    --brand-red: #d90a0a;
    --deep-red: #8e0000;
    --steel: #a8a8a8;
    --white: #ffffff;
  }
  * { margin: 0; padding: 0; box-sizing: border-box; }
  html, body { width: 1200px; height: 1200px; overflow: hidden; background: var(--ink-dark); }
  .ad {
    position: relative;
    width: 1200px; height: 1200px;
    overflow: hidden;
    font-family: "Roboto Condensed", Arial, sans-serif;
    color: var(--white);
  }
  .engine-photo {
    position: absolute; inset: 0;
    background: radial-gradient(ellipse at 60% 30%, #4a4a4a 0%, #2c2c2c 45%, #151515 100%);
  }
  .base-band { position: absolute; inset: 0; }
  .brand-name {
    position: absolute; left: 94px; top: 70px;
    font-family: "Montserrat", Arial, sans-serif;
    font-weight: 600; font-size: 34px; letter-spacing: 6px;
    color: var(--brand-red);
  }
  .headline {
    position: absolute; left: 66px; top: 258px;
    font-weight: 700; line-height: 1; text-transform: uppercase;
  }
  .headline .line-one { display: block; font-size: 84px; letter-spacing: -1px; }
  .headline .line-two { display: block; font-family: "Arimo", Arial, sans-serif; font-size: 80px; margin-top: 4px; letter-spacing: -1px; }
  .divider { position: absolute; top: 446px; left: 68px; display: flex; gap: 7px; }
  .divider span { width: 101px; height: 4px; }
  .divider .gray { background: var(--steel); }
  .divider .white { background: var(--white); }
  .divider .red { background: var(--brand-red); }
  .service-point {
    position: absolute; left: 78px; top: 496px;
    display: flex; gap: 10px; align-items: flex-start;
    font-weight: 500; font-size: 18.5px; line-height: 24px;
  }
  .service-point svg { flex: none; margin-top: 2px; }
  .phone-box {
    position: absolute; left: 68px; top: 574px;
    width: 475px; height: 80px; border-radius: 6px;
    background: var(--brand-red);
    font-weight: 700; font-size: 60px; line-height: 80px;
    padding-left: 20px;
  }
  .van-photo {
    position: absolute; left: 478px; top: 451px;
    width: 722px; height: 700px;
  }
  .website {
    position: absolute; left: 66px; top: 1072px;
    font-family: Arial, sans-serif; font-size: 27px;
  }
</style>
</head>
<body>
<main class="ad">
  <div class="engine-photo" role="img" aria-label="Dark monochrome close-up of a car engine bay"></div>

  <svg class="base-band" width="1200" height="1200" viewBox="0 0 1200 1200" aria-hidden="true">
    <defs>
      <linearGradient id="redFill" x1="0" y1="0" x2="1" y2="1">
        <stop offset="0" stop-color="#e00d0d"/>
        <stop offset="1" stop-color="#7e0000"/>
      </linearGradient>
    </defs>
    <polygon points="0,982 1200,641 1200,651 0,992" fill="#9a9a9a"/>
    <polygon points="0,992 1200,651 1200,1200 0,1200" fill="url(#redFill)"/>
  </svg>

  <div class="brand-name">KELLBRIGHT MOTORWORKS</div>

  <h1 class="headline">
    <span class="line-one">Kellbright Motorworks</span>
    <span class="line-two">Comes to you</span>
  </h1>

  <div class="divider"><span class="gray"></span><span class="white"></span><span class="red"></span></div>

  <p class="service-point">
    <svg width="22" height="22" viewBox="0 0 22 22" aria-hidden="true">
      <path d="M19 8.5A9 9 0 1 1 14.5 2.8" fill="none" stroke="#d90a0a" stroke-width="2.2" stroke-linecap="round"/>
      <path d="M6.5 10.5l4 4L20 4.5" fill="none" stroke="#d90a0a" stroke-width="2.4" stroke-linecap="round" stroke-linejoin="round"/>
    </svg>
    <span>We do all types of auto maintenance/repair on customer<br>vehicles at their home/office or wherever!</span>
  </p>

  <div class="phone-box">(940) 572-9163</div>

  <svg class="van-photo" viewBox="0 0 722 700" role="img" aria-label="White branded service van parked, seen from the front three-quarter view">
    <defs>
      <linearGradient id="vanTone" x1="0" y1="0" x2="1" y2="1">
        <stop offset="0" stop-color="#f2f2f2"/>
        <stop offset="1" stop-color="#b9b9b9"/>
      </linearGradient>
    </defs>
    <path d="M60 300 L300 240 L520 10 L722 0 L722 520 L480 560 L420 700 L250 690 L220 600 L20 580 L0 420 Z" fill="url(#vanTone)"/>
  </svg>

  <div class="website">www.kellbrightmotorworks.com</div>
</main>
</body>
</html>
```